Irrigation Business needs their business cards modernised and revamped

I would like to keep my current logo, colours and revamp the format of the card.

I would like the card to be clean yet important.

Im not sure if you include texture but i would like the named logo to be indented into the card etc.

show me something alive and free something thats clinical to the point yet has a feel of achievement. i would like people to go nice card.

Target Market(s)

high end clients, corporate, sports field manger, the guys that make the decisions

Industry/Entity Type

Business

Contact Information for Business Card

nformation to be included

Dorian Hesk (Director)
0487253916
dorian@tfcraft.biz
www.taddsfieldcrafts.com

instagram logo
google logo
facebook logo

Colors

Designer to choose colors to be used in the design.

Requirements
Nice to have
• indentations a really nice feel to the card good texture

```html
<!DOCTYPE html>
<html lang="en">
<head>
<meta charset="utf-8">
<title>Tadds Field Crafts — Business Card</title>
<link href="https://fonts.googleapis.com/css2?family=Roboto:wght@400;700&display=swap" rel="stylesheet">
<style>
  :root{
    --stage:#2b2b2d;
    --paper:#f7f7f7;
    --brand-blue:#1f5fa8;
    --deep-blue:#1c4f95;
    --sky-blue:#3fa6db;
    --field-green:#22893a;
    --ink:#1d2a1d;
    --white:#ffffff;
  }
  *{margin:0;padding:0;box-sizing:border-box}
  html,body{width:1200px;height:997px;overflow:hidden;background:var(--stage);font-family:"Roboto",Arial,sans-serif}
  .card{position:absolute;width:640px;height:366px;border-radius:22px;overflow:hidden;background:var(--paper);box-shadow:0 12px 30px rgba(0,0,0,.45)}
  .card--back{left:280px;top:70px;display:flex;align-items:center;justify-content:center;gap:26px}
  .card--front{left:280px;top:520px}
  .brand-dot{flex:none;width:120px;height:120px;border-radius:50%;background:var(--sky-blue)}
  .brand-name{color:var(--brand-blue);font-weight:700;text-transform:uppercase;letter-spacing:.5px;white-space:nowrap}
  .card--back .brand-name{font-size:38px;line-height:1.05;white-space:normal;width:240px}
  .front-art{position:absolute;inset:0;width:100%;height:100%}
  .front-brand{position:absolute;top:40px;left:0;right:0;display:flex;flex-direction:column;align-items:center;gap:10px}
  .front-brand .brand-dot{width:50px;height:50px}
  .front-brand .brand-name{font-size:27px}
  .holder{position:absolute;top:157px;left:0;right:0;text-align:center}
  .holder-name{color:var(--white);font-weight:700;font-size:17px;letter-spacing:.5px}
  .holder-role{color:var(--ink);font-size:13px;margin-top:2px}
  .website{position:absolute;right:30px;top:250px;color:var(--white);font-size:14px;letter-spacing:.3px}
  .contacts{position:absolute;left:28px;top:262px;list-style:none;color:var(--white);font-size:15px}
  .contacts li{display:flex;align-items:flex-start;gap:12px;margin-bottom:7px;line-height:1.2}
  .icon{flex:none;width:19px;height:19px;border-radius:50%;background:var(--field-green);display:flex;align-items:center;justify-content:center}
  .icon svg{width:11px;height:11px;fill:var(--white)}
</style>
</head>
<body>
  <div class="card card--back">
    <span class="brand-dot"></span>
    <span class="brand-name">Tadds Field Crafts</span>
  </div>

  <div class="card card--front">
    <svg class="front-art" viewBox="0 0 640 366" preserveAspectRatio="none" aria-hidden="true">
      <polygon fill="var(--deep-blue)" points="0,208 170,208 200,232 440,232 470,208 640,208 640,366 0,366"/>
      <polygon fill="var(--field-green)" points="0,196 190,196 215,150 425,150 450,196 640,196 640,208 470,208 440,232 200,232 170,208 0,208"/>
    </svg>

    <div class="front-brand">
      <span class="brand-dot"></span>
      <span class="brand-name">Tadds Field Crafts</span>
    </div>

    <div class="holder">
      <p class="holder-name">DORIAN HESK</p>
      <p class="holder-role">Director</p>
    </div>

    <p class="website">www.taddsfieldcrafts.com</p>

    <ul class="contacts">
      <li><span class="icon"><svg viewBox="0 0 24 24"><path d="M6.6 10.8a15.1 15.1 0 006.6 6.6l2.2-2.2a1 1 0 011-.25 11.4 11.4 0 003.6.57 1 1 0 011 1V20a1 1 0 01-1 1A17 17 0 013 4a1 1 0 011-1h3.5a1 1 0 011 1c0 1.25.2 2.45.57 3.570a1 1 0 01-.25 1z"/></svg></span>0487253916</li>
      <li><span class="icon"><svg viewBox="0 0 24 24"><path d="M2 5h20v14H2zm2 2v.4l8 5 8-5V7l-8 5z"/></svg></span>dorian@tfcraft.biz</li>
      <li><span class="icon"><svg viewBox="0 0 24 24"><path d="M12 2a7 7 0 00-7 7c0 5.2 7 13 7 13s7-7.8 7-13a7 7 0 00-7-7zm0 9.5A2.5 2.5 0 1112 6.5a2.5 2.5 0 010 5z"/></svg></span>PO Box 318 Kelvale<br>B.C. QLD 4417</li>
    </ul>
  </div>
</body>
</html>
```